Ha4Giggle website

We need a website called Ha 4 Giggle (ha4giggle.com).
This site is for fun (just like 7lol.com, flopdiary.com, chucklepapa.com etc. You know what I mean, right?)
so we are open to different designs/looks. We are looking for a simple and clean and fun design to make it easy to use for our users.

The design of Ha4Giggle should be different from other fun site (better than others, I mean), and this is what we want you to do.

The style for our site should be in (or be similar to, at least) the BLOG way, (If you can't catch my words, have a look at 7LOL or Flopdiary).

But at meantime, I'd like to stress again that we want this site be different from the sites like 7LOL and FlopDiary.
Updates

i have a logo for the website now.

http://images.artmarketo.com/designs/56722_788142_42200_thumbnail.jpg

pls try to fit this logo into the website design.

Requirements
Must have
• We need at least following pages designed:

1. front page (index.jpg)

2. login form page (login.jpg)

3. registeration form page (register.jpg)

4. content page (post.jpg)

5. submit photo form page (submit.jpg)

6. user profile page (user_center.jpg)

```html
<!DOCTYPE html>
<html lang="en">
<head>
<meta charset="utf-8">
<title>Ha4Giggle</title>
<link rel="stylesheet" href="https://fonts.googleapis.com/css2?family=Oswald:wght@400;500&family=Libre+Baskerville&family=Open+Sans:ital,wght@0,400;0,600;0,700;1,400&family=Fredoka:wght@600&display=swap">
<style>
:root{
  --header:#3b3b3b; --header-dark:#2a2a2a; --nav:#232323; --page:#efefef;
  --panel:#ffffff; --blue:#0aa5df; --blue-dark:#0a8fc4; --soft-blue:#c3e6f4;
  --text:#444; --muted:#888; --meta-bg:#ebebeb; --footer:#13a4d6; --white:#fff;
}
*{box-sizing:border-box;margin:0;padding:0}
html,body{width:840px;height:1200px;overflow:hidden}
body{position:relative;background:var(--page);font-family:"Open Sans",sans-serif;color:var(--text)}
.abs{position:absolute}
.header{left:0;top:0;width:840px;height:61px;background:linear-gradient(#454545,#333)}
.logo{font-family:"Fredoka",sans-serif;font-weight:600;color:var(--white);font-size:30px;letter-spacing:-.5px}
.login{left:619px;top:0;width:65px;height:61px;background:var(--header-dark);color:var(--white);font-size:10px;font-weight:700;text-align:center;padding-top:16px}
.bookmark{left:700px;top:16px;width:104px;color:#ccc;font-size:10px;font-weight:600;text-align:center}
.nav{left:0;top:61px;width:840px;height:45px;background:var(--nav)}
.nav-item{top:75px;font-family:"Oswald",sans-serif;font-size:14px;color:#ddd;letter-spacing:.5px}
.nav-sep{top:61px;width:1px;height:45px;background:#3a3a3a}
.mini{height:10px;padding:0 3px;font-size:6px;line-height:10px;border:1px solid #bbb;background:#f4f4f4;color:#2c5a9e;border-radius:2px}
.mini.plus{background:#d33;color:#fff;border-color:#d33}
.count{height:10px;padding:0 3px;font-size:6px;line-height:10px;border:1px solid #ccc;background:#fff;color:#333}
.search{left:620px;top:74px;width:171px;height:20px;background:var(--white);border:1px solid #ccc;font-size:8px;font-style:italic;color:#aaa;padding:4px 12px}
.tab{top:126px;height:24px;width:63px;background:var(--blue);color:var(--white);font-size:10px;font-weight:700;text-align:center;line-height:24px;border-radius:2px}
.tab.active{background:#333}
.main{left:41px;top:164px;width:553px;height:878px;background:var(--panel);border:1px solid #ddd}
.post-title{left:60px;font-family:"Libre Baskerville",serif;font-size:14.5px;color:#555}
.meta{left:61px;width:505px;height:21px;background:var(--meta-bg);font-size:8px;font-style:italic;color:var(--muted);padding:5px 14px;word-spacing:2px}
.excerpt{left:61px;top:244px;width:505px;font-size:10px;line-height:16px;color:#555}
.dotted{left:61px;width:505px;border-top:1px dotted #ccc}
.stats{left:63px;font-size:8px;color:var(--muted);display:flex;gap:10px;align-items:center}
.shares{display:flex;gap:3px;left:428px}
.pager{left:230px;top:1010px;display:flex;gap:3px}
.pager span{height:17px;min-width:16px;padding:0 4px;border:1px solid var(--blue);font-size:8px;line-height:15px;text-align:center;color:#2c6fa6;background:var(--white)}
.pager .current{background:var(--blue-dark);color:var(--white)}
.pager .plain{border:none;background:none}
.pager .off{border-color:#ccc;color:#999}
.social-box{left:608px;top:126px;width:196px;height:88px;background:var(--blue);border-radius:2px;color:var(--white);font-size:9.5px;padding:10px 10px}
.social-row{display:flex;align-items:center;gap:7px;margin-top:10px;font-size:8.5px;font-weight:600}
.newsletter{left:610px;top:474px;width:192px;height:122px;background:var(--soft-blue);padding:10px 10px}
.nl-title{font-family:"Oswald",sans-serif;font-size:17px;color:#1a86b6;letter-spacing:.3px}
.input{left:623px;top:536px;width:164px;height:19px;background:var(--white);border:1px solid #bbb;font-size:8.5px;font-style:italic;color:#999;padding:3px 7px}
.submit{left:724px;top:562px;width:62px;height:21px;background:var(--blue-dark);color:var(--white);font-size:9px;font-weight:700;text-align:center;line-height:21px}
.pop-title{left:612px;top:614px;font-family:"Libre Baskerville",serif;font-size:15px;color:#1a93c7}
.pop-line{left:612px;top:644px;width:198px;height:2px;background:var(--blue)}
.pop-date{left:614px;font-size:8.5px;font-style:italic;color:#555}
.pop-text{left:614px;width:186px;font-size:8.5px;line-height:12px;color:#222}
.pop-text b{font-weight:400;color:var(--blue-dark);font-size:7.5px}
.more{left:757px;top:853px;width:48px;height:14px;background:#777;color:var(--white);font-size:7px;font-weight:700;text-align:center;line-height:14px}
.footer{left:0;top:1066px;width:840px;height:134px;background:var(--footer)}
.foot-links{left:73px;top:1081px;font-size:9.5px;color:var(--white);word-spacing:3px}
.foot-rule{left:56px;top:1105px;width:517px;height:1px;background:rgba(255,255,255,.5)}
.foot-col{top:1111px;font-size:8px;color:var(--white);line-height:14.5px}
.foot-col h4{font-weight:400;font-size:9.5px;margin-bottom:3px}
.foot-col li{list-style:none}
.foot-col li::before{content:"› ";font-weight:700}
.foot-info{left:600px;width:193px;text-align:center;color:var(--white);font-size:8.5px}
</style>
</head>
<body>
<header class="abs header"></header>
<div class="abs logo" style="left:38px;top:8px">Ha4Giggle</div>
<div class="abs login">LOG IN
  <svg width="16" height="16" viewBox="0 0 16 16" style="display:block;margin:5px auto 0"><circle cx="8" cy="5" r="3.5" fill="#ddd"/><path d="M1 15c0-5 14-5 14 0z" fill="#ddd"/></svg>
</div>
<div class="abs bookmark">ADD BOOKMARK
  <svg width="16" height="16" viewBox="0 0 16 16" style="display:block;margin:4px auto 0"><path d="M8 1l2.1 4.6 5 .5-3.8 3.3 1.1 4.9L8 11.8 3.6 14.3l1.1-4.9L.9 6.1l5-.5z" fill="#888"/></svg>
</div>

<nav class="abs nav"></nav>
<div class="abs nav-item" style="left:41px;color:#fff">UPLOAD</div>
<div class="abs nav-sep" style="left:99px"></div>
<div class="abs nav-item" style="left:114px">FAST</div>
<div class="abs nav-sep" style="left:156px"></div>
<div class="abs nav-item" style="left:171px">FUN</div>
<div class="abs" style="left:506px;top:78px;display:flex;gap:4px">
  <span class="mini">Like</span><span class="mini">Tweet</span><span class="mini plus">+1</span>
</div>
<div class="abs search">Search</div>

<div class="abs tab active" style="left:41px">Fun</div>
<div class="abs tab" style="left:107px">Hot</div>
<div class="abs tab" style="left:174px">Video</div>
<div class="abs tab" style="left:239px">Vote</div>

<main class="abs main"></main>

<h2 class="abs post-title" style="top:186px">Donec cursus ultricies erat, quis dignissim</h2>
<div class="abs meta" style="top:214px">David, &nbsp;2 mints ago, &nbsp;May 11, 2012</div>
<p class="abs excerpt">Etiam condimentum lacinia bibendum. Sed tempor feugiat purus, idetsen dapibus eros sagittis sed nulla lacina. Pellentesque habitant morbi laciros.</p>
<div class="abs" role="img" aria-label="Ad photo: dog on a floor with ants" style="left:63px;top:289px;width:259px;height:171px;background:linear-gradient(135deg,#cfd7d8,#c79a4c 50%,#b9c4c6)"></div>
<div class="abs" role="img" aria-label="Ad photo: bridge ending at a cliff over the sea" style="left:322px;top:289px;width:242px;height:171px;background:linear-gradient(#c7d0d6,#8a9aa3 55%,#6f7d5c)"></div>
<div class="abs" role="img" aria-label="Ad illustration: pipette shaped object" style="left:63px;top:460px;width:259px;height:178px;background:radial-gradient(circle at 60% 45%,#6d6d6d,#ededed 45%,#f3f3f3)"></div>
<div class="abs" role="img" aria-label="Ad photo: eggplant sharpened like a pencil" style="left:322px;top:460px;width:242px;height:178px;background:radial-gradient(circle at 45% 45%,#6a3f63,#eeeeee 40%,#f2f2f2)"></div>
<div class="abs dotted" style="top:650px"></div>
<div class="abs stats" style="top:658px"><span>💬 15 Comments</span><span>♥ 17 Likes</span></div>
<div class="abs shares" style="top:658px"><span class="mini">Like</span><span class="count">26</span><span class="mini">Tweet</span><span class="count">97</span><span class="mini plus">+1</span><span class="count">26</span></div>
<div class="abs dotted" style="top:678px"></div>

<h2 class="abs post-title" style="top:699px">Donec cursus ultricies erat, quis dignissim</h2>
<div class="abs meta" style="top:727px">David, &nbsp;2 mints ago, &nbsp;May 11, 2012</div>
<div class="abs" role="img" aria-label="Photo: rock band on a smoky stage in backlight" style="left:62px;top:762px;width:504px;height:192px;background:radial-gradient(ellipse at 50% 45%,#e4e4e4,#6a6a6a 25%,#111 60%,#000)"></div>
<div class="abs dotted" style="top:966px"></div>
<div class="abs stats" style="top:973px"><span>💬 15 Comments</span><span>♥ 17 Likes</span></div>
<div class="abs shares" style="top:973px"><span class="mini">Like</span><span class="count">26</span><span class="mini">Tweet</span><span class="count">97</span><span class="mini plus">+1</span><span class="count">26</span></div>
<div class="abs dotted" style="top:992px"></div>

<div class="abs pager">
  <span class="off">« Previous</span><span class="current">1</span><span>2</span><span>3</span><span>4</span><span>5</span><span>6</span><span>7</span><span>8</span><span>9</span><span>10</span><span class="plain">. . . .</span><span>212</span><span>213</span><span style="font-weight:700">Next »</span>
</div>

<aside class="abs social-box">
  Show how much you like Funny things!
  <div class="social-row"><span class="mini">Like</span><span>3,078,410 people like this.</span></div>
  <div class="social-row"><span class="mini">Tweet</span><span>312 people Follow this.</span></div>
</aside>
<div class="abs" role="img" aria-label="Advertisement: runner's legs with a new-revolution race banner" style="left:610px;top:230px;width:192px;height:230px;background:linear-gradient(#9cbf7a,#e9e4dc 45%,#e2dcd2 80%,#111 80%)"></div>

<section class="abs newsletter">
  <div class="nl-title">SIGN UP FOR NEWSLETTER</div>
  <div style="font-size:8.5px;color:#333;margin-top:1px">Sign up to receive our free newsletters!</div>
</section>
<div class="abs input">Email Address</div>
<div class="abs submit">SUBMIT</div>

<h3 class="abs pop-title">Popular posts</h3>
<div class="abs pop-line"></div>
<div class="abs pop-date" style="top:659px">May 10th 2012</div>
<p class="abs pop-text" style="top:677px">Lorem ipsum dolor sit amet conse ctetur adipiscing elit &nbsp;<b>READ MORE</b></p>
<div class="abs dotted" style="left:614px;width:190px;top:716px"></div>
<div class="abs pop-date" style="top:730px">May 10th 2012</div>
<p class="abs pop-text" style="top:748px">Lorem ipsum dolor sit amet conse ctetur adipiscing elit &nbsp;<b>READ MORE</b></p>
<div class="abs dotted" style="left:614px;width:190px;top:788px"></div>
<div class="abs pop-date" style="top:802px">May 10th 2012</div>
<p class="abs pop-text" style="top:820px">Lorem ipsum dolor sit amet conse ctetur adipiscing elit &nbsp;<b>READ MORE</b></p>
<div class="abs more">MORE +</div>

<footer class="abs footer"></footer>
<div class="abs foot-links">Home &nbsp;| &nbsp;About Us &nbsp;| &nbsp;Upload &nbsp;| &nbsp;Fast &nbsp;| &nbsp;Fun &nbsp;| &nbsp;Hot &nbsp;| &nbsp;Video &nbsp;| &nbsp;Vote &nbsp;| &nbsp;Member Login &nbsp;| &nbsp;Sitemap</div>
<div class="abs foot-rule"></div>
<ul class="abs foot-col" style="left:67px"><h4>Footer Links</h4><li>Consectetur</li><li>Mauris ideaui</li><li>Aunc vivera ornare</li><li>Nunc convallis</li></ul>
<ul class="abs foot-col" style="left:204px"><h4>Footer Links</h4><li>Consectetur</li><li>Mauris ideaui</li><li>Aunc vivera ornare</li><li>Nunc convallis</li></ul>
<ul class="abs foot-col" style="left:341px"><h4>Footer Links</h4><li>Consectetur</li><li>Mauris ideaui</li><li>Aunc vivera ornare</li><li>Nunc convallis</li></ul>
<ul class="abs foot-col" style="left:478px"><h4>Footer Links</h4><li>Consectetur</li><li>Mauris ideaui</li><li>Aunc vivera ornare</li><li>Nunc convallis</li></ul>
<div class="abs foot-info logo" style="top:1076px;font-size:30px">Ha4Giggle</div>
<div class="abs foot-info" style="top:1130px">Copyright © 2012 www.ha4giggle.com</div>
<div class="abs foot-info" style="top:1147px">All rights reserved</div>
<svg class="abs" style="left:662px;top:1167px" width="72" height="22" viewBox="0 0 72 22">
  <circle cx="11" cy="11" r="10" fill="#fff"/><circle cx="35" cy="11" r="10" fill="#fff"/><circle cx="59" cy="11" r="10" fill="#fff"/>
</svg>
</body>
</html>
```